Electrical needs letterhead design

Need a letterhead design for an electrical company. Using the same colours as to what are used in the logo.
After a modern design.

Want the logo in top right or top left.

Must include...

ABN 71 804 239 356
PHONE 0458203917
www.kelmaroo.com.au
jed@kelmaroo.com.au

'ABN' and 'PHONE' in bold.

Keep it basic. Logo top left, details either next to it or far right corner. Dont want any other objects included.

Electrical

```html
<!DOCTYPE html>
<html lang="en">
<head>
<meta charset="utf-8">
<title>Kelmaroo Stationery</title>
<link rel="stylesheet" href="https://fonts.googleapis.com/css2?family=Arimo:wght@400;700&family=Open+Sans:wght@400;600&family=Questrial&display=swap">
<style>
  :root {
    --backdrop: #ececec;
    --paper: #f7f7f6;
    --brand-red: #a02c24;
    --brand-red-light: #cc4a3a;
    --brand-grey: #7a7a7a;
    --ink: #3a3a3a;
    --rule: #8a8a8a;
    --cell-fill: #e4e4e4;
    --fax-title: #555555;
  }
  * { box-sizing: border-box; margin: 0; padding: 0; }
  html, body { width: 1200px; height: 815px; overflow: hidden; }
  body { background: var(--backdrop); position: relative; font-family: "Arimo", Arial, sans-serif; color: var(--ink); }

  .sheet { position: absolute; top: 70px; width: 483px; height: 682px; background: var(--paper); }
  .sheet--letterhead { left: 80px; }
  .sheet--fax { left: 638px; }

  .brand { position: absolute; left: 38px; top: 66px; display: flex; align-items: center; gap: 6px; }
  .brand__dot { width: 9px; height: 9px; border-radius: 50%; background: var(--brand-red); }
  .brand__name { font-family: "Open Sans", Arial, sans-serif; font-weight: 600; font-size: 29px; line-height: 1; color: var(--brand-red); letter-spacing: -0.3px; }

  .contact { position: absolute; left: 37px; top: 637px; font-family: "Questrial", Arial, sans-serif; font-size: 7px; line-height: 8px; color: var(--ink); }
  .contact__label { font-family: "Arimo", Arial, sans-serif; font-weight: 700; color: var(--brand-red); }
  .abn { position: absolute; right: 44px; top: 653px; font-family: "Questrial", Arial, sans-serif; font-size: 7px; color: var(--ink); }
  .abn b { font-family: "Arimo", Arial, sans-serif; font-weight: 700; }

  .footer-band { position: absolute; left: 0; bottom: 0; width: 100%; height: 13px; display: flex; gap: 2px; }
  .footer-band__grey { flex: 1; background: var(--brand-grey); }
  .footer-band__red { flex: 1; background: linear-gradient(90deg, var(--brand-red), var(--brand-red-light)); }

  .fax-title { position: absolute; right: 42px; top: 46px; font-family: "Arimo", Arial, sans-serif; font-size: 62px; line-height: 1; color: var(--fax-title); }

  .fax-details { position: absolute; left: 37px; top: 143px; width: 405px; border-collapse: collapse; font-size: 7px; }
  .fax-details td { border: 1px solid var(--rule); height: 14.7px; padding: 0 4px; }
  .fax-details .label { font-weight: 700; width: 42px; }
  .fax-details .value { width: 161px; }

  .fax-flags { position: absolute; left: 37px; top: 231px; width: 405px; height: 16px; display: flex; border: 1px solid var(--rule); background: var(--cell-fill); }
  .fax-flags__item { display: flex; align-items: center; justify-content: center; gap: 3px; font-size: 7px; font-weight: 700; color: #555; border-right: 1px solid var(--rule); }
  .fax-flags__item:last-child { border-right: 0; }
  .fax-flags__box { width: 5px; height: 5px; border: 0.8px solid #666; background: var(--paper); }

  .fax-comments { position: absolute; left: 37px; top: 246px; width: 405px; height: 372px; border: 1px solid var(--rule); border-top: 0; }
  .fax-comments__label { text-align: center; margin-top: 11px; font-size: 7.5px; color: #555; }
</style>
</head>
<body>

<section class="sheet sheet--letterhead">
  <div class="brand"><span class="brand__name">Kelmaroo</span><span class="brand__dot"></span></div>
  <div class="contact">
    <div><span class="contact__label">Phone:</span> 0458203917</div>
    <div><span class="contact__label">Email:</span> jed@kelmaroo.com.au</div>
    <div>www.kelmaroo.com.au</div>
  </div>
  <div class="abn"><b>ABN</b> 71 804 239 356</div>
  <div class="footer-band"><span class="footer-band__grey"></span><span class="footer-band__red"></span></div>
</section>

<section class="sheet sheet--fax">
  <div class="brand"><span class="brand__name">Kelmaroo</span><span class="brand__dot"></span></div>
  <div class="fax-title">FAX</div>

  <table class="fax-details">
    <tr><td class="label">To:</td><td class="value"></td><td class="label">From:</td><td class="value"></td></tr>
    <tr><td class="label">Fax:</td><td class="value"></td><td class="label">Pages:</td><td class="value"></td></tr>
    <tr><td class="label">Phone:</td><td class="value"></td><td class="label">Date:</td><td class="value"></td></tr>
    <tr><td class="label">Re:</td><td class="value"></td><td class="label">CC:</td><td class="value"></td></tr>
  </table>

  <div class="fax-flags">
    <div class="fax-flags__item" style="width:81px"><span class="fax-flags__box"></span>Urgent</div>
    <div class="fax-flags__item" style="width:77px"><span class="fax-flags__box"></span>For Review</div>
    <div class="fax-flags__item" style="width:91px"><span class="fax-flags__box"></span>Please Comment</div>
    <div class="fax-flags__item" style="width:75px"><span class="fax-flags__box"></span>Please Reply</div>
    <div class="fax-flags__item" style="flex:1"><span class="fax-flags__box"></span>Please Recycle</div>
  </div>

  <div class="fax-comments"><p class="fax-comments__label">COMMENTS:</p></div>

  <div class="contact">
    <div><span class="contact__label">Phone:</span> 0458203917</div>
    <div><span class="contact__label">Email:</span> jed@kelmaroo.com.au</div>
    <div>www.kelmaroo.com.au</div>
  </div>
  <div class="abn"><b>ABN</b> 71 804 239 356</div>
  <div class="footer-band"><span class="footer-band__grey"></span><span class="footer-band__red"></span></div>
</section>

</body>
</html>
```